Need website redesign!

I have a site, www.pinehavenfitcamp.example

I am looking to have it redesigned to make it simpler, and encourage people who hit the home page to click on a service, opt in, or contact me for more info. Having a video front and center with icons representing the services we offer around it may be a good idea, but I am open to YOUR design. Conversion is my goal. I want it to be friendly, but convey the fun and ENERGY of my bootcamp. Scrolling pics on home page so people can get a feel for our bootcamp is recommended as well.

```html
<!DOCTYPE html>
<html lang="en">
<head>
<meta charset="utf-8">
<title>Pinehaven Fit Camp</title>
<link rel="stylesheet" href="https://fonts.googleapis.com/css2?family=Oswald:wght@400;500;600&family=Arimo:wght@400;700&display=swap">
<style>
:root{
  --page:#1c1c1c;
  --shell:#161616;
  --panel:#222;
  --panel-head:#2a2a2a;
  --line:#333;
  --red:#e8321a;
  --white:#fff;
  --text:#9a9a9a;
  --muted:#6d6d6d;
  --date-bg:#3a3a3a;
}
*{box-sizing:border-box;margin:0;padding:0}
html,body{width:742px;height:1200px;overflow:hidden}
body{position:relative;background:var(--page);font-family:"Arimo",Arial,sans-serif;color:var(--text);font-size:7px;line-height:1.45}
.side-photo{position:absolute;top:0;height:520px;width:180px;background:radial-gradient(ellipse at 50% 40%,#5a5a5a 0%,#303030 55%,#1c1c1c 100%)}
.topband{position:absolute;left:0;top:0;width:742px;height:98px;background:linear-gradient(#111,#1a1a1a)}
.shell{position:absolute;left:102px;top:70px;width:540px;height:1064px;background:var(--shell);box-shadow:0 0 18px #000}
.util{position:absolute;left:414px;top:0;width:204px;height:24px;background:linear-gradient(#3a3a3a,#262626);display:flex;justify-content:space-around;align-items:center;font-size:6.5px;color:#aaa;border-radius:0 0 3px 3px}
.brand{position:absolute;left:102px;top:20px;font-family:"Oswald",sans-serif;font-weight:600;color:var(--white);line-height:1}
.brand .small{font-size:13px;display:block}
.brand .big{font-size:22px;display:block;margin-top:2px}
.tagline{position:absolute;left:422px;top:43px;font-family:"Oswald",sans-serif;font-size:8px;color:#eee;letter-spacing:.3px}
.cta-top{position:absolute;left:560px;top:37px;width:80px;height:22px;border-radius:11px;background:var(--red);color:#fff;font-family:"Oswald",sans-serif;font-size:9px;display:flex;align-items:center;justify-content:center}
.nav{position:absolute;left:102px;top:70px;width:540px;height:28px;background:linear-gradient(#2e2e2e,#1e1e1e);display:flex;align-items:center;padding-left:10px;gap:17px;font-family:"Oswald",sans-serif;font-size:9px;color:#ddd;border-bottom:1px solid #000}
.nav .on{color:var(--red)}
.hero{position:absolute;left:102px;top:98px;width:540px;height:212px;background:linear-gradient(100deg,#8a8a8a 0%,#5c5c5c 40%,#a0a0a0 70%,#6b6b6b 100%)}
.hero-text{position:absolute;left:134px;top:214px;font-family:"Oswald",sans-serif;color:#fff}
.hero-text .l1{font-size:17px;display:block}
.hero-text .l2{font-size:17px;color:var(--red);background:rgba(20,20,20,.75);padding:0 6px;display:inline-block;margin:3px 0 3px 10px}
.hero-text .l3{font-size:17px;display:block;margin-left:56px}
.optin{position:absolute;left:466px;top:154px;width:162px;height:140px}
.optin p{font-size:9.5px;color:#fff;line-height:1.25;padding-left:6px}
.optin .red{color:var(--red);font-family:"Oswald",sans-serif;font-size:11px}
.optin-box{position:absolute;left:0;top:52px;width:162px;height:88px;background:rgba(20,20,20,.85);padding:7px 8px}
.field{height:20px;background:#fff;color:#444;font-size:8px;padding:5px 8px;margin-bottom:6px}
.btn-red{background:var(--red);color:#fff;font-family:"Oswald",sans-serif;font-size:9.5px;height:21px;display:flex;align-items:center;justify-content:center}
.card{position:absolute;top:319px;width:166px;height:143px;background:var(--panel)}
.head{height:24px;background:var(--panel-head);font-family:"Oswald",sans-serif;font-size:9.5px;color:#eee;padding:5px 8px;border-bottom:1px solid #111}
.photo{background:linear-gradient(135deg,#5a5a5a,#2c2c2c)}
.card .photo{position:absolute;left:0;top:26px;width:166px;height:117px}
.card .label{position:absolute;left:0;top:95px;background:var(--red);color:#fff;font-size:11px;padding:3px 6px;width:110px}
.panel{position:absolute;background:var(--panel)}
.news-item{position:absolute;width:155px}
.news-item h4{font-size:8px;color:#fff;margin:4px 0 3px}
.date{display:inline-block;background:var(--date-bg);color:#ddd;font-size:6.5px;padding:2px 5px;font-weight:700}
.more{color:var(--muted);font-size:6px;margin-top:2px}
.sched{position:absolute;left:6px;width:154px;height:20px;background:#1a1a1a;display:flex;align-items:center;font-size:7.5px;color:#ddd;padding:0 5px;gap:6px}
.sched .t{margin-left:auto;font-size:6.5px}
.cls{position:absolute;top:754px;width:115px}
.cls .photo{height:80px}
.cls .cap{position:absolute;left:0;top:68px;font-size:6.5px;color:#eee;background:rgba(0,0,0,.55);padding:1px 4px}
.cls h4{font-size:9px;color:#fff;margin:6px 0 3px;font-weight:700}
.arrows{position:absolute;left:592px;top:722px;display:flex;gap:3px}
.arrows span{width:15px;height:15px;border-radius:50%;background:#444}
.foot-col{position:absolute;top:930px;width:150px}
.foot-col h3{font-family:"Oswald",sans-serif;font-size:9.5px;color:#eee;font-weight:500;margin-bottom:6px}
.foot-col .red-h{color:var(--red);font-family:"Oswald",sans-serif;font-size:11px;margin:2px 0}
.foot-col p{font-size:6.5px;margin-bottom:5px}
.foot-col .hl{color:#ddd;font-weight:700}
.time{color:#888;font-size:7.5px;font-weight:700}
.pill{display:inline-block;background:var(--red);color:#fff;font-family:"Oswald",sans-serif;font-size:8.5px;padding:4px 9px;border-radius:10px}
.plain-btn{display:inline-block;background:#444;color:#eee;font-family:"Oswald",sans-serif;font-size:8px;padding:4px 6px;margin-top:4px}
.bottom-nav{position:absolute;left:102px;top:1150px;display:flex;gap:14px;font-family:"Oswald",sans-serif;font-size:7.5px;color:#ccc}
.follow{position:absolute;left:102px;top:1169px;display:flex;align-items:center;gap:5px;font-family:"Oswald",sans-serif;font-size:8px;color:#ccc}
.follow i{display:block;width:14px;height:14px;background:#555}
.copy{position:absolute;left:512px;top:1172px;font-size:6.5px;color:#888}
.totop{position:absolute;left:612px;top:1148px;display:flex;align-items:center;gap:4px;font-size:6px;color:#888}
.totop span{width:15px;height:15px;border-radius:50%;background:#555}
</style>
</head>
<body>
<div class="side-photo" style="left:0" role="img" aria-label="Photo of a muscular athlete in shadow"></div>
<div class="side-photo" style="right:0" role="img" aria-label="Photo of a muscular athlete in shadow"></div>
<div class="topband"></div>
<div class="shell"></div>

<div class="util"><span>Blog</span><span>Team</span><span>News</span><span>Log In</span><span>Search</span></div>
<div class="brand"><span class="small">PINEHAVEN</span><span class="big">FIT CAMP</span></div>
<div class="tagline">1 WEEK CAN TRANSFORM YOUR SELF</div>
<div class="cta-top">START TODAY ›</div>

<nav class="nav"><span class="on">HOME</span><span>BLOG</span><span>NEWS</span><span>CLASSES</span><span>FACILITIES</span><span>GALLERY</span><span>TEAM</span><span>ABOUT US</span><span>CONTACT US</span></nav>

<div class="hero" role="img" aria-label="Photo of a group workout class training hard"></div>
<div class="hero-text"><span class="l1">Programs</span><span class="l2">Members only workouts</span><span class="l3">and event and more</span></div>
<div class="optin">
  <p>Leave your email for a<br>FREE week of bootcamp,</p>
  <p class="red">NO OBLIGATION</p>
  <div class="optin-box">
    <div class="field">Your Name</div>
    <div class="field">Your Email</div>
    <div class="btn-red">Get Started Now</div>
  </div>
</div>

<div class="card" style="left:113px"><div class="head">START TODAY</div><div class="photo" role="img" aria-label="Photo of a man on a rowing machine"></div><div class="label">Vestibulum ante</div></div>
<div class="card" style="left:288px"><div class="head">WHAT'S NEW ?</div><div class="photo" role="img" aria-label="Photo of a man lifting in the gym"></div><div class="label">Enas egettellus</div></div>
<div class="card" style="left:464px"><div class="head">SPECIAL OFFERS</div><div class="photo" role="img" aria-label="Photo of a woman training with a barbell" style="background:linear-gradient(135deg,#c8703a,#7a4a2a)"></div><div class="label">Suspendisse</div></div>

<div class="panel" style="left:113px;top:474px;width:342px;height:228px">
  <div class="head">GYM NEWS</div>
  <div class="news-item" style="left:10px;top:34px">
    <div class="photo" role="img" aria-label="Photo of an outdoor group stretch" style="height:60px;background:linear-gradient(#7aa0c0,#5c8a3a)"></div>
    <h4>Praesent convallis ultric...</h4>
    <p>Praesent convallis ultrices dui, vitae tincidunt mi tincidunt non. Vestibulum eu velit at eros porttitor vestibulum quis id justo. Phasellus semper tincidunt posuere. Praesent pharetra turpis id sapien tristique suscipit. Fusce pellentesque mauris ut odio tincidunt nec porttitor lectus tempor. Ut ac sodales dui. Phasellus nisl ...</p>
    <div class="more">› Read More</div>
  </div>
  <div class="news-item" style="left:178px;top:34px">
    <span class="date">December 4th, 2012</span>
    <h4>Lorem ipsum dolor sit ame...</h4>
    <p>Lorem ipsum dolor sit amet, consectetur adipiscing elit. Nunc ut amet massa enim. Maecenas nisl orci, Curabitur fringilla lobortis felis, a feugiat sapien molestie vel. Vestibulum ante ipsum primis in fauc ...</p>
    <div class="more">› Read More</div>
    <div style="height:8px"></div>
    <span class="date">December 4th, 2012</span>
    <h4>Vestibulum nibh leo, pulv...</h4>
    <p>Praesent vitae tortor est, nam vitae laoreet mauris. Nulla purus felis, consectetur vitae posuere nec, dapibus at quam. Nullam rutrum arcu in luctus accumsan malesuada semper eros ultricies. Sed blandit turpis ...</p>
    <div class="more">› Read More</div>
  </div>
</div>

<div class="panel" style="left:464px;top:474px;width:166px;height:220px">
  <div class="head">SPECIAL OFFERS</div>
  <div class="photo" role="img" aria-label="Photo of an indoor cycling class" style="position:absolute;left:6px;top:30px;width:154px;height:110px;background:linear-gradient(135deg,#9a7a5a,#4a3a2a)"></div>
  <div class="sched" style="top:145px"><svg width="10" height="10" viewBox="0 0 10 10"><circle cx="5" cy="5" r="4" fill="none" stroke="#888"/><path d="M5 2.5V5h2" stroke="#888" fill="none"/></svg>Maecenas erat ...<span class="t">1:30am - 2:30am</span></div>
  <div class="sched" style="top:168px"><svg width="10" height="10" viewBox="0 0 10 10"><circle cx="5" cy="5" r="4" fill="none" stroke="#888"/><path d="M5 2.5V5h2" stroke="#888" fill="none"/></svg>Pellentesque a...<span class="t">7:30am - 8:30am</span></div>
  <div class="sched" style="top:191px"><svg width="10" height="10" viewBox="0 0 10 10"><rect x="1" y="2" width="8" height="7" fill="none" stroke="#888"/><path d="M1 4h8" stroke="#888"/></svg>View All Classes</div>
</div>

<div class="panel" style="left:113px;top:716px;width:517px;height:192px">
  <div class="head">OUR FITNESS CLASSES</div>
</div>
<div class="arrows"><span></span><span></span></div>
<div class="cls" style="left:124px"><div class="photo" role="img" aria-label="Photo of a group posing outdoors" style="background:linear-gradient(#5a8a4a,#3a5a3a)"></div><span class="cap">2016-04-06 to 2016-04-06</span><h4>Morbi interdum rhonc...</h4><p>Lorem ipsum dolor sit amet, consectetur adipiscing elit. Maecenas erat nunc, sollicitudin sit amet mattis non, ... Read More</p></div>
<div class="cls" style="left:250px"><div class="photo" role="img" aria-label="Photo of a woman doing floor exercise"></div><span class="cap">2016-04-06 to 2016-04-06</span><h4>Pellentesque auctor ...</h4><p>Lorem ipsum dolor sit amet, consectetur adipiscing elit. Maecenas erat nunc, sollicitudin sit amet mattis non, ... Read More</p></div>
<div class="cls" style="left:376px"><div class="photo" role="img" aria-label="Photo of suspension strap training"></div><span class="cap">2016-04-06 to 2016-04-06</span><h4>Maecenas adipiscing ...</h4><p>Lorem ipsum dolor sit amet, consectetur adipiscing elit. Maecenas erat nunc, sollicitudin sit amet mattis non, ... Read More</p></div>
<div class="cls" style="left:502px"><div class="photo" role="img" aria-label="Photo of an outdoor boot camp session" style="background:linear-gradient(#8ab0c8,#4a7a3a)"></div><span class="cap">2016-04-06 to 2016-04-06</span><h4>Vivamus leo odio vul...</h4><p>Lorem ipsum dolor sit amet, consectetur adipiscing elit. Maecenas erat nunc, sollicitudin sit amet mattis non, ... Read More</p></div>

<div class="foot-col" style="left:113px">
  <h3>CONTACT INFO</h3>
  <p>48 Larchmont Row, Suite 2, Pinehaven 20417</p>
  <p class="hl">Call Now: (555) 014-2260</p>
  <p class="hl">Email: hello@pinehavenfitcamp.example</p>
  <p style="color:var(--red);font-weight:700">Daily Timing: 06:00 to 21:00<br>Sunday: 08:00 to 14:00</p>
  <h3>ABOUT PINEHAVEN</h3>
  <p>Lorem ipsum dolor sit amet, consectetur adipiscing elit. Nulla tincidunt fringilla suscipit.</p>
</div>
<div class="foot-col" style="left:288px">
  <h3>Latest Tweets</h3>
  <p><span class="time">2 Hours Ago</span><br>"I like to try with people...they ask me what I do...I tell them I listen to music" Mara Ellison #CreativeDays clipshare.example/watch?v=EY00hL</p>
  <p><span class="time">6 Hours Ago</span><br>For 2 years Tallwood Studio has supported @HarborLightAid - giving hope to women in local violence crisis. inside.tallwood.example/support... #giving</p>
  <p><span class="time">10 Hours Ago</span><br>In Pinehaven and getting started with code? Come along to Code Meetup (4 February)! codemeetup.example/pinehaven #meetup</p>
  <span class="pill">FOLLOW US ON CHIRPER</span>
</div>
<div class="foot-col" style="left:464px">
  <h3>MEMBERSHIP PROMOTIONS</h3>
  <div class="red-h">GET 25% DISCount</div>
  <p>Lorem ipsum dolor sit amet, consectetur adipiscing elit. Nulla tincidunt fringilla suscipit. Praesent dapibus risus mauris. Cras libero nunc, vestibulum eu rutrum sagittis, dapibus non justo. Praesent dapibus risus mauris.</p>
  <div class="red-h">Join Today</div>
  <p>Lorem ipsum dolor sit amet, consectetur adipiscing elit. Nulla tincidunt fringilla suscipit. Praesent dapibus risus mauris. Nulla tincidunt fringilla suscipit.</p>
  <span class="plain-btn">MEMBERSHIP PLANS</span>
</div>

<div class="bottom-nav"><span>HOME</span><span>BLOG</span><span>NEWS</span><span>CLASSES</span><span>FACILITIES</span><span>GALLERY</span><span>TEAM</span><span>ABOUT US</span><span>CONTACT US</span></div>
<div class="totop">Top <span></span></div>
<div class="follow">Follow Us <i></i><i></i><i></i><i></i></div>
<div class="copy">© 2014 Pinehaven Fit Camp</div>
</body>
</html>
```